Radiant Stage Productions Sole Brillante Concert

I want a PORTRAIT STYLE DL size poster for a cabaret-style concert that I am promoting as part of a Community Arts Festival in Western Australia.

I WOULD LIKE A RED CHECK TABLECLOTH WITH PICNIC FOOD AND A WINE GLASS TOWARDS THE BOTTOM OF THE PAGE . WITH THE BLACK AND WHITE IMAGE OF THE MAN NOT TOO LARGE . BRIGHT RED WHITE AND GREEN COLOURS TO SHOW THE ITALIAN THEME.

The name of the concert is "Sole Brillante" which means the heart of Italy, my Italian Heart , I love italy etc.

The concert will have live music, with a 6 or 7 piece band. A variety of singers will performing lots of lovely Italian songs in different styles from Grand Opera to the songs of the 40's an 50's (Walt Brennor and Lloyd Haverty) through to modern Italian popular songs like Under the Evening Sky (Nel Vento Blu etc) it will be like a party with everyone coming on and singing their favourite Italian songs and we want the audience to sing along and have a great time.

It is important that the reader understands that they can sit and enjoy a picnic and wine package . Included in the price.
Patrons will be sitting at tables looking forward to the action on the stage.

**********************************************************************************
Text For the poster...
Radiant Stage Productions ( small font size at top of the page)

Sole Brillante! (this is the name of the concert)

Cabaret at the Harbourgate Civic Hall (the word cabaret shows that is a catered event)

"Maestro Pietro Galvani takes us on a fun filled journey from the Isle of Sicily to the canals of Venezia"

Sunday 10th November 2013
Matinee 3:00pm

Tickets
STANDARD $45 Upstairs Gallery
PREMIUM $95 Downstairs at tables with wine and gourmet picnic hamper included.

www.seatpoint-example.com.au
tel: 1300 415 908
For further info
www.loretta-bellweather.example
facebook Loretta Bellweather Concert Club
*************************************************************************************
THIS IS THE TEXT THAT IS GOING IN THE ARTS BROCHURE FOR YOUR INFORMATION : "Celebrating the best of all things Italian. Maestro Pietro Galvani takes us on a fun filled journey with his band and vocalists through various styles of Italian music and favourite classic songs. From the Isle of Sicily to the canals of Venezia, you won't be able to stop yourself singing along to these famous tunes!"

Hello Everyone,

The deadline has been extended to Wednesday.

I have updated some of the info for the brief details below.

NOTE: I have added a description of the event
decided not to have a keyboard or piano image.

I want bold colours with Italian Flag or Green, White and Red .

Clear text so the eye flows down the page to the information details.

Thanks

Target Market(s)

40 + age group...Fremantle has a very strong Italian Community we will be directly targeting the Italian Clubs in Fremantle and the Perth areas. The Musical director is well known in these clubs.

Industry/Entity Type

Club

Requirements
Must have
• The Coastline Arts Festival Tab.
Nice to have
• important that the picnic and wine element is highlighted and that there are tables. I don't want them thinking it is an outdoors event.
Bright vibrant colours
An Italian flag?

```html
<!DOCTYPE html>
<html lang="en">
<head>
<meta charset="utf-8">
<title>Sole Brillante! – Cabaret at the Harbourgate Civic Hall</title>
<link rel="stylesheet" href="https://fonts.googleapis.com/css2?family=Poppins:wght@400;600;700&display=swap">
<style>
  :root {
    --flag-red: #c8322a;
    --flag-white: #f2f2ef;
    --flag-green: #2f8a3a;
    --title-red: #c23a1f;
    --cabaret-green: #2d7a1f;
    --tab-white: #ffffff;
    --ink: #111111;
    --text-white: #ffffff;
    --photo-grey: #8a8a8a;
    --photo-dark: #3a3a3a;
    --cloth-red: #b5302c;
  }
  * { margin: 0; padding: 0; box-sizing: border-box; }
  html, body { width: 1200px; height: 2548px; overflow: hidden; background: #ffffff; }
  .poster {
    position: relative; width: 1200px; height: 2548px; overflow: hidden;
    font-family: "Poppins", sans-serif; color: var(--text-white);
    background: linear-gradient(180deg, #a9a9a9 0%, #9a9a9a 60%, #6c6c6c 100%);
  }
  .flag { position: absolute; left: 0; top: 0; width: 1200px; height: 1500px; display: flex; }
  .flag__band { flex: 1; }
  .flag__band--red { background: linear-gradient(180deg, var(--flag-red) 0%, #c9544c 40%, rgba(170,170,170,0) 100%); }
  .flag__band--white { background: linear-gradient(180deg, #ffffff 0%, var(--flag-white) 40%, rgba(170,170,170,0) 100%); }
  .flag__band--green { background: linear-gradient(180deg, var(--flag-green) 0%, #5a9c60 40%, rgba(170,170,170,0) 100%); }

  .festival-tab {
    position: absolute; left: 82px; top: 0; width: 204px; height: 642px;
    background: var(--tab-white); color: var(--ink);
  }
  .festival-tab__council {
    position: absolute; left: 0; top: 60px; width: 204px; text-align: center;
    font-weight: 600; font-size: 26px; line-height: 1.15;
  }
  .festival-tab__council::before {
    content: ""; display: block; width: 46px; height: 46px; margin: 0 auto 10px;
    border-radius: 50%; background: var(--ink);
  }
  .festival-tab__rule { position: absolute; left: 46px; top: 230px; width: 3px; height: 380px; background: var(--ink); }
  .festival-tab__label {
    position: absolute; left: 64px; top: 236px; writing-mode: vertical-rl;
    font-weight: 700; font-size: 33px; line-height: 1.05; text-transform: uppercase;
  }

  .presenter {
    position: absolute; left: 430px; top: 40px; width: 400px; text-align: center;
    font-size: 42px; line-height: 1.1; color: var(--text-white);
  }
  .title {
    position: absolute; left: 0; top: 760px; width: 1200px; text-align: center;
    font-weight: 700; font-size: 98px; color: var(--title-red); letter-spacing: -1px;
  }
  .title-rule { position: absolute; left: 107px; top: 908px; width: 990px; height: 2px; background: #5a5a5a; }
  .venue {
    position: absolute; left: 0; top: 920px; width: 1200px; text-align: center;
    font-size: 50px; color: var(--cabaret-green);
  }
  .venue strong { font-weight: 700; }
  .journey {
    position: absolute; left: 130px; top: 1095px; width: 940px; text-align: center;
    font-size: 43px; line-height: 1.28; text-shadow: 0 2px 6px rgba(0,0,0,0.45);
  }
  .journey strong { font-weight: 700; }

  .portrait {
    position: absolute; left: 400px; top: 1290px; width: 600px; height: 900px;
    background: radial-gradient(ellipse at 50% 35%, #cfcfcf 0%, var(--photo-grey) 45%, var(--photo-dark) 100%);
    border-radius: 280px 280px 0 0;
  }
  .tablecloth {
    position: absolute; left: 0; top: 2130px; width: 1200px; height: 418px;
    background: linear-gradient(180deg, #c8615d 0%, var(--cloth-red) 55%, #7e201d 100%);
  }

  .tickets {
    position: absolute; right: 40px; top: 1725px; width: 760px; text-align: right;
    font-size: 43px; line-height: 1.36; text-shadow: 0 2px 6px rgba(0,0,0,0.6);
  }
  .tickets__heading { font-weight: 700; }
  .date {
    position: absolute; left: 220px; top: 2070px; width: 900px;
    text-shadow: 0 2px 6px rgba(0,0,0,0.6);
  }
  .date__day { font-weight: 700; font-size: 51px; line-height: 1.2; }
  .date__time { font-size: 55px; line-height: 1.1; padding-left: 400px; }
  .contact {
    position: absolute; left: 42px; top: 2210px; width: 800px;
    font-size: 34px; line-height: 1.42; text-shadow: 0 2px 5px rgba(0,0,0,0.7);
  }
  .contact strong { font-weight: 700; }
</style>
</head>
<body>
<main class="poster">
  <div class="flag" aria-hidden="true">
    <div class="flag__band flag__band--red"></div>
    <div class="flag__band flag__band--white"></div>
    <div class="flag__band flag__band--green"></div>
  </div>

  <aside class="festival-tab">
    <div class="festival-tab__council">City of<br>Port Calloway</div>
    <div class="festival-tab__rule"></div>
    <div class="festival-tab__label">A City of<br>Port Calloway<br>Festival Event</div>
  </aside>

  <p class="presenter">Radiant Stage<br>Productions</p>

  <h1 class="title">Sole Brillante!</h1>
  <div class="title-rule"></div>
  <p class="venue"><strong>Cabaret</strong> at the Harbourgate Civic Hall</p>

  <p class="journey"><strong>Maestro Pietro Galvani</strong> takes us on<br>a fun filled journey from the Isle of Sicily<br>to the canals of Venezia.</p>

  <div class="portrait" role="img" aria-label="Black and white photograph of the smiling maestro in a dark shirt"></div>
  <div class="tablecloth" role="img" aria-label="Red check tablecloth with a picnic basket, food and a glass of red wine"></div>

  <section class="tickets">
    <p class="tickets__heading">Tickets:</p>
    <p>• STANDARD $45 Upstairs Gallery</p>
    <p>• PREMIUM $95 Downstairs at<br>tables with wine and gourmet<br>picnic hamper included.</p>
  </section>

  <div class="date">
    <p class="date__day">Sunday 10th November 2013</p>
    <p class="date__time">Matinee 3:00pm</p>
  </div>

  <section class="contact">
    <p><strong>www.seatpoint-example.com.au</strong></p>
    <p>tel: <strong>1300 415 908</strong></p>
    <p>For further info</p>
    <p><strong>www.loretta-bellweather.example</strong></p>
    <p>facebook <strong>Loretta Bellweather Concert Club</strong></p>
  </section>
</main>
</body>
</html>
```